Refresh of graphic design for existing website

We would like to refresh our website. Please see the attached design specifications.

Industry/Entity Type

Graphic Design

```html
<!DOCTYPE html>
<html lang="en">
<head>
<meta charset="utf-8">
<title>Torque &amp; Gauge Alliance</title>
<link rel="stylesheet" href="https://fonts.googleapis.com/css2?family=Open+Sans:wght@400;600;700&family=PT+Serif:wght@400;700&display=swap">
<style>
:root{
  --green:#3b9a5c;
  --green-dark:#2c7d48;
  --green-text:#5fc27f;
  --header:#1d1d1d;
  --dark:#2a2a2a;
  --hero:#3a3f44;
  --light:#e6e6e6;
  --card:#ffffff;
  --ink:#333333;
  --muted:#666666;
  --white:#ffffff;
}
*{margin:0;padding:0;box-sizing:border-box}
html,body{width:872px;height:1200px;overflow:hidden}
body{position:relative;font-family:"Open Sans",Arial,sans-serif;background:var(--dark);color:var(--white)}

.site-header{position:absolute;left:0;top:0;width:872px;height:90px;background:var(--header)}
.brand{position:absolute;left:87px;top:10px}
.brand-tagline{font-size:13px;font-weight:600;color:var(--white)}
.brand-name{display:flex;align-items:center;gap:8px;margin-top:4px;font-size:42px;font-weight:700;line-height:1;color:var(--white)}
.brand-name .mark{width:14px;height:14px;border-radius:50%;background:var(--green)}
.login{position:absolute;left:470px;top:14px;display:flex;gap:8px;align-items:center;font-size:11px}
.login input{width:90px;height:16px;border:0;background:var(--white)}
.login .submit{height:16px;padding:0 10px;background:#555;color:var(--white);font-size:10px;line-height:16px}
.login-links{position:absolute;left:770px;top:40px;font-size:10px;line-height:14px;text-align:left}

.main-nav{position:absolute;left:87px;top:90px;width:700px;height:24px;background:var(--green);display:flex;justify-content:space-around;align-items:center}
.main-nav a{color:var(--white);text-decoration:none;font-size:10px;font-weight:700;letter-spacing:.3px}

.hero{position:absolute;left:0;top:114px;width:872px;height:290px;background:linear-gradient(90deg,#2d3236,#4a5055 60%,#3a3f44)}
.hero-photo{position:absolute;left:450px;top:20px;width:260px;height:260px;border-radius:50%;border:5px solid #cfd3d6;background:radial-gradient(circle at 55% 45%,#5b7fa5,#2f4a66 70%)}
.hero-text{position:absolute;left:140px;top:60px;width:300px}
.hero-text h1{font-family:"PT Serif",Georgia,serif;font-weight:400;font-size:38px;line-height:1.05;color:var(--green-text)}
.hero-text p{margin-top:12px;font-size:11px;line-height:16px;color:#e0e0e0}
.btn{display:inline-block;margin-top:14px;padding:6px 16px;background:var(--green);color:var(--white);border-radius:4px;font-size:11px;font-weight:600}
.arrow{position:absolute;top:128px}
.arrow.prev{left:30px}
.arrow.next{left:822px}

.features{position:absolute;left:0;top:404px;width:872px;height:316px;background:var(--light)}
.feature{position:absolute;top:62px;width:162px;height:206px;background:var(--card);text-align:center;color:var(--ink);border:1px solid #d0d0d0}
.feature.active{background:var(--green);color:var(--white);border-color:var(--green-dark)}
.feature .icon{width:72px;height:62px;margin:14px auto 8px;background:linear-gradient(135deg,#8fb3d6,#3b6c9c)}
.feature.active .icon{background:linear-gradient(135deg,#6fa7d8,#2f5f95)}
.feature h2{font-family:"PT Serif",Georgia,serif;font-weight:400;font-size:22px;line-height:22px;text-transform:uppercase}
.feature p{margin:8px 14px 0;font-size:9px;line-height:12px;color:var(--muted)}
.feature.active p{color:#e9f6ee}
.pager{position:absolute;left:432px;top:288px;width:8px;height:8px;border-radius:50%;background:#999}

.latest{position:absolute;left:0;top:720px;width:872px;height:385px}
.latest-title{position:absolute;left:87px;top:18px;width:698px;display:flex;align-items:center;gap:16px;font-family:"PT Serif",Georgia,serif;font-size:22px;color:var(--white)}
.latest-title::before,.latest-title::after{content:"";flex:1;height:1px;background:#888}
.work{position:absolute;width:215px;height:142px;border:3px solid #cfd3d6}
.work .photo{width:100%;height:100%}
.work .caption{position:absolute;left:0;bottom:6px;width:100%;text-align:center;font-size:9px;font-weight:700;color:var(--white)}
.work.hl{border-color:var(--green)}

.site-footer{position:absolute;left:0;top:1105px;width:872px;height:95px;background:var(--green);text-align:center;font-size:10px;color:var(--white)}
.site-footer .copy{margin-top:30px}
.site-footer .addr{margin-top:10px}
</style>
</head>
<body>
<header class="site-header">
  <div class="brand">
    <div class="brand-tagline">Torque &amp; Gauge Alliance</div>
    <div class="brand-name">TGA<span class="mark"></span></div>
  </div>
  <form class="login">
    <label>Email:</label><input type="text" aria-label="Email">
    <label>Password:</label><input type="password" aria-label="Password">
    <span class="submit">Submit</span>
  </form>
  <div class="login-links">Remember me<br>Contact us<br>Forgot Password</div>
</header>

<nav class="main-nav">
  <a>HOME</a><a>ABOUT US</a><a>MEMBERSHIP</a><a>TGA MEMBERS</a><a>TGA EVENTS</a><a>THE TGA LIBRARY</a><a>MARKET RESEARCH</a><a>VIDEOS &amp; FILES</a>
</nav>

<section class="hero">
  <div class="hero-photo" role="img" aria-label="Technician working under the hood of a car"></div>
  <div class="hero-text">
    <h1>Cursus penati saccum nulla.</h1>
    <p>Professional tools, trusted service and shared know-how for every workshop. Our members build better repairs through training, research and events held across the year.</p>
    <span class="btn">Read More</span>
  </div>
  <svg class="arrow prev" width="20" height="30" viewBox="0 0 20 30"><path d="M15 3 L5 15 L15 27" fill="none" stroke="#ddd" stroke-width="3"/></svg>
  <svg class="arrow next" width="20" height="30" viewBox="0 0 20 30"><path d="M5 3 L15 15 L5 27" fill="none" stroke="#ddd" stroke-width="3"/></svg>
</section>

<section class="features">
  <div class="feature" style="left:87px">
    <div class="icon" role="img" aria-label="Conference audience illustration"></div>
    <h2>Industry<br>Events</h2>
    <p>Browse upcoming shows, training days and meetings planned for the coming season.</p>
  </div>
  <div class="feature active" style="left:265px">
    <div class="icon" role="img" aria-label="News screen illustration"></div>
    <h2>Breaking<br>News</h2>
    <p>Read the latest updates from across the service and tool industry today.</p>
  </div>
  <div class="feature" style="left:443px">
    <div class="icon" role="img" aria-label="Shopping cart illustration"></div>
    <h2>Market<br>Deals</h2>
    <p>Find member offers and special prices on equipment, software and shop supplies.</p>
  </div>
  <div class="feature" style="left:621px">
    <div class="icon" role="img" aria-label="Puzzle pieces illustration"></div>
    <h2>Join<br>TGA</h2>
    <p>Become a member and connect with leading tool makers and service experts.</p>
  </div>
  <span class="pager"></span>
</section>

<section class="latest">
  <h2 class="latest-title">LATEST WORK</h2>
  <div class="work" style="left:87px;top:62px"><div class="photo" role="img" aria-label="Mechanic in protective gear at work" style="background:linear-gradient(135deg,#4a6f99,#1f2f45)"></div><div class="caption">LOREM IPSUM DOLOR</div></div>
  <div class="work" style="left:327px;top:62px"><div class="photo" role="img" aria-label="Hand writing on a clipboard" style="background:linear-gradient(135deg,#d8d4c8,#7a7468)"></div><div class="caption">LOREM IPSUM DOLOR</div></div>
  <div class="work" style="left:567px;top:62px"><div class="photo" role="img" aria-label="Technician inspecting an engine" style="background:linear-gradient(135deg,#5f7f9f,#2b3540)"></div><div class="caption">LOREM IPSUM DOLOR</div></div>
  <div class="work" style="left:87px;top:222px"><div class="photo" role="img" aria-label="Digital diagnostic display of a car" style="background:linear-gradient(135deg,#3a78b8,#12243d)"></div><div class="caption">LOREM IPSUM DOLOR</div></div>
  <div class="work hl" style="left:327px;top:222px"><div class="photo" role="img" aria-label="Car dashboard interior" style="background:linear-gradient(135deg,#6b6b6b,#222)"></div><div class="caption">LOREM IPSUM DOLOR</div></div>
  <div class="work" style="left:567px;top:222px"><div class="photo" role="img" aria-label="Vehicle interior with steering wheel" style="background:linear-gradient(135deg,#8a8f96,#2f3338)"></div><div class="caption">LOREM IPSUM DOLOR</div></div>
</section>

<footer class="site-footer">
  <p class="copy">Copyright © 2024 Torque &amp; Gauge Alliance. All rights reserved.</p>
  <p class="addr">TGA · 48 Harbor Lane, Suite 210 · Millbrook, OR 97000 · 555-014-2280</p>
</footer>
</body>
</html>
```